Strategy and Technology Consulting - Our Story and Values Page

Interior Page design – Our History and Our Values

Our homepage has been designed and we are looking for a design for one of the interior pages. This interior page tells the story of Our History and Our Values

Because the homepage has been designed, we would like this interior page to reflect the design of the homepage without being a mirror image of the homepage.

This site will be implemented in WordPress using the Elementor framework.

Font: Poppins medium and Poppins dark
Illustrations: Our homepage illustrations were designed by “Teslo 1964” on Imagevale. Compatible original or stock illustrations are welcome. Stock photography is also welcome. Teslo is also available through Teslo Bramen on Portvue

• Homepage design – this is the design we will use for our homepage. Contest entries should reflect this basic style but should be distinctly different from the homepage.
• Our History and Our Values – Wireframe – the basic layout of the page we are looking for.
• Our History and Our Values – Word document with the text supporting the wireframe.
• Color Palette – please use colors compatible with the palette attached.

Our Story - timeline
There is a timeline element in the wireframe. The wireframe displays this as a series of chevrons (arrows), but it does not need to be. Creativity in display of the timeline is appreciated.

Our Values
If you look at the Word document, you will see that there are a lot of words on the page. The winning design will present the information in a way that engages the user without overwhelming them with too much to read. For example, they may click on a value and see more information.

Target Market(s)

CIO's and Technology Executives

Number of Pages Required

1 page

Font styles to use
Sans Serif
Other font styles liked:
• Poppin

Requirements
Must have
• A timeline element, all of our values
Nice to have
• Clever timeline display

```html
<!DOCTYPE html>
<html lang="en">
<head>
<meta charset="utf-8">
<title>Veltrion – Our Story &amp; Values</title>
<link href="https://fonts.googleapis.com/css2?family=Poppins:wght@300;400;500;600;700;800&display=swap" rel="stylesheet">
<style>
:root{
  --navy:#3d4d66;
  --navy-deep:#2f3e52;
  --link:#2f4d70;
  --yellow:#f0b51a;
  --card:#e6edf4;
  --tl-head:#bcd8ef;
  --tl-blue:#a3b8c7;
  --tl-grey:#6f7d7f;
  --muted:#4f5e70;
  --footer-top:#3e4d67;
  --footer-bottom:#5d728d;
  --bar:#3a475e;
  --white:#ffffff;
}
*{margin:0;padding:0;box-sizing:border-box}
html,body{width:1200px;height:3407px;overflow:hidden}
body{position:relative;font-family:"Poppins",sans-serif;background:var(--white);color:var(--navy)}
a{color:inherit;text-decoration:none}

/* Header */
.site-header{position:absolute;top:0;left:0;width:1200px;height:94px;border-bottom:1px solid #eef1f5}
.brand{position:absolute;left:85px;top:20px;font-size:44px;font-weight:300;color:#8b95a0;letter-spacing:.5px}
.main-nav{position:absolute;left:543px;top:37px;display:flex;align-items:center;gap:22px;font-size:12.5px;font-weight:600;color:var(--navy)}
.main-nav .caret{display:inline-block;width:6px;height:6px;border-right:1.5px solid var(--navy);border-bottom:1.5px solid var(--navy);transform:rotate(45deg) translateY(-3px);margin-left:5px}
.btn-contact{position:absolute;left:982px;top:28px;width:133px;height:37px;border-radius:19px;background:var(--yellow);color:var(--white);font-size:11.5px;font-weight:700;display:flex;align-items:center;justify-content:center}

.section-title{position:absolute;left:84px;font-size:54px;font-weight:700;color:var(--navy)}

/* Timeline */
.timeline-line{position:absolute;left:83px;top:314px;width:1028px;border-top:2px dotted #a9bdd0}
.timeline-dot{position:absolute;width:8px;height:8px;border-radius:50%;background:#a9bdd0;top:311px}
.era{position:absolute;top:296px;width:234px;height:201px;color:var(--white)}
.era-year{height:39px;background:var(--tl-head);color:var(--link);font-size:28px;font-weight:400;display:flex;align-items:center;justify-content:center;position:relative}
.era-year::after{content:"";position:absolute;left:50%;bottom:-8px;margin-left:-8px;border:8px solid transparent;border-bottom:0;border-top-color:var(--tl-head)}
.era-body{height:162px;padding:23px 19px 0;font-size:11.5px;line-height:17.5px;font-weight:300}
.era-body strong{font-weight:600}
.era-link{position:absolute;left:19px;top:170px;font-size:11px;font-weight:600;text-decoration:underline}
.era--blue .era-body{background:var(--tl-blue)}
.era--grey .era-body{background:var(--tl-grey)}
.story-art{position:absolute;left:860px;top:242px;width:284px;height:281px;border-radius:50% 46% 42% 40%;background:radial-gradient(circle at 55% 45%,#f5d67a 0,#c7d8e8 45%,rgba(231,238,245,0) 72%)}

/* Values */
.values-rule{position:absolute;left:410px;top:630px;width:701px;border-top:2px dotted #a9bdd0}
.values-dot{position:absolute;left:1108px;top:626px;width:8px;height:8px;border-radius:50%;background:#a9bdd0}
.value-card{position:absolute;left:83px;width:1035px;height:139px;background:var(--card);box-shadow:0 6px 10px rgba(60,80,110,.18)}
.value-title{position:absolute;left:40px;top:34px;font-size:28px;font-weight:400;color:var(--navy-deep)}
.value-text{position:absolute;left:40px;top:86px;font-size:11.5px;color:var(--muted)}
.value-text a{font-weight:600;color:var(--link);text-decoration:underline;margin-left:3px}
.value-art{position:absolute;right:20px;top:-48px;width:220px;height:188px;border-radius:46% 54% 8px 8px}
.value-card::after{content:"";position:absolute;right:10px;bottom:0;width:260px;border-bottom:2px solid #3f6aa8}

/* Waves & newsletter */
.waves{position:absolute;left:0;top:2280px;width:1200px;height:1071px}
.newsletter{position:absolute;left:136px;top:2696px;width:925px;height:208px;border-radius:104px;background:var(--yellow)}
.newsletter h2{position:absolute;left:81px;top:56px;font-size:33px;font-weight:800;color:var(--white)}
.newsletter p{position:absolute;left:81px;top:108px;font-size:15px;line-height:19px;font-weight:500;color:var(--white)}
.subscribe{position:absolute;left:549px;top:82px;width:320px;height:44px;border-radius:22px;background:var(--white);display:flex;align-items:center;padding-left:24px;font-size:12.5px;color:#8a95a3}
.subscribe svg{margin-right:8px}
.subscribe-btn{position:absolute;right:4px;top:4px;width:36px;height:36px;border-radius:50%;background:#8fa7bf;display:flex;align-items:center;justify-content:center}

/* Footer */
.footer-brand{position:absolute;left:119px;top:3082px;font-size:60px;font-weight:300;color:var(--white)}
.social{position:absolute;top:3166px;width:32px;height:32px;border-radius:50%;background:#7e92aa}
.footer-contact{position:absolute;left:214px;top:3228px;width:130px;height:36px;border-radius:18px;background:var(--yellow);color:var(--white);font-size:11px;font-weight:700;display:flex;align-items:center;justify-content:center}
.footer-col{position:absolute;top:3058px;color:var(--white)}
.footer-col h3{font-size:19px;font-weight:700;margin-bottom:16px}
.footer-col li{list-style:none;font-size:12.5px;font-weight:400;height:31px}
.footer-col li::before{content:"›";margin-right:7px}
.contact-item{display:flex;gap:9px;font-size:12.5px;line-height:17.5px;margin-bottom:18px}
.contact-item svg{flex:none;margin-top:2px}
.bottom-bar{position:absolute;left:0;top:3351px;width:1200px;height:56px;background:var(--bar);color:var(--white);font-size:12.5px;font-weight:500;display:flex;align-items:center;justify-content:center}
.chat{position:absolute;left:1134px;top:3296px;width:48px;height:48px;border-radius:50%;background:var(--yellow);display:flex;align-items:center;justify-content:center}
</style>
</head>
<body>

<header class="site-header">
  <div class="brand">Veltrion</div>
  <nav class="main-nav">
    <svg width="15" height="13" viewBox="0 0 15 13"><path d="M7.5 0 15 6.5h-2V13H9V9H6v4H2V6.5H0z" fill="#8b95a0"/></svg>
    <a>ABOUT US<span class="caret"></span></a>
    <a>SERVICES<span class="caret"></span></a>
    <a>INSIGHTS<span class="caret"></span></a>
    <a>JOIN US<span class="caret"></span></a>
  </nav>
  <a class="btn-contact">CONTACT US</a>
</header>

<h1 class="section-title" style="top:140px">Our Story</h1>

<div class="timeline-line"></div>
<div class="timeline-dot" style="left:80px"></div>
<div class="timeline-dot" style="left:1108px"></div>

<article class="era era--blue" style="left:126px">
  <div class="era-year">2017 – 2019</div>
  <div class="era-body">Growth Strategy Focus<br>Consistent, Modest Growth<br>Preliminary Focus on Technology<br><strong>Eureka!</strong><br>Implementing strategy is hard.</div>
  <a class="era-link">VIEW DETAIL</a>
</article>
<article class="era era--grey" style="left:397px">
  <div class="era-year">2020 – 2021</div>
  <div class="era-body">Pandemic Pauses Growth<br>Rethinking :<br>- the business model<br>- the delivery model</div>
  <a class="era-link">VIEW DETAIL</a>
</article>
<article class="era era--blue" style="left:668px">
  <div class="era-year">2022 -&gt;</div>
  <div class="era-body">Leadership Team for Focus on<br>Essential Areas<br>Rapid Growth<br>Customer Success</div>
  <a class="era-link">VIEW DETAIL</a>
</article>
<div class="story-art" role="img" aria-label="Illustration of a consultant working at a laptop desk on an office chair"></div>

<h2 class="section-title" style="top:588px">Our Values</h2>
<div class="values-rule"></div>
<div class="values-dot"></div>

<section class="value-card" style="top:708px">
  <h3 class="value-title">The Value of Every Human. Regardless.</h3>
  <p class="value-text">Each person's unique experiences and perspectives add vibrant hues to the tapestry of our shared existence..<a>VIEW DETAIL</a></p>
  <div class="value-art" role="img" aria-label="Illustration of a stopwatch surrounded by notification and media icons" style="background:radial-gradient(circle at 50% 58%,#f2c23a 0,#c8d9ea 38%,rgba(230,237,244,0) 70%)"></div>
</section>
<section class="value-card" style="top:945px">
  <h3 class="value-title">Collaboration</h3>
  <p class="value-text">Collaboration in work transforms individual endeavors into symphonies of collective achievement..<a>VIEW DETAIL</a></p>
  <div class="value-art" role="img" aria-label="Illustration of a team fitting puzzle pieces together" style="background:linear-gradient(160deg,#b9a7d8 0,#8fa6bf 40%,#f0c23c 80%,#e6edf4 100%);opacity:.75"></div>
</section>
<section class="value-card" style="top:1187px">
  <h3 class="value-title">Passion</h3>
  <p class="value-text">Passion infuses our work with energy, transforming routine tasks into opportunities for creativity and innovation..<a>VIEW DETAIL</a></p>
  <div class="value-art" role="img" aria-label="Illustration of a woman with flowing hair among leaves" style="background:radial-gradient(circle at 50% 45%,#6f7880 0,#bcd6ee 45%,rgba(230,237,244,0) 72%)"></div>
</section>
<section class="value-card" style="top:1429px">
  <h3 class="value-title">Excellence</h3>
  <p class="value-text">Excellence isn't a destination; it's a continuous journey of refinement and growth..<a>VIEW DETAIL</a></p>
  <div class="value-art" role="img" aria-label="Illustration of a runner in motion" style="background:radial-gradient(circle at 48% 48%,#e9b53a 0,#c6d8ec 42%,rgba(230,237,244,0) 72%)"></div>
</section>
<section class="value-card" style="top:1671px">
  <h3 class="value-title">Tenacity</h3>
  <p class="value-text">Tenacity is the unwavering anchor that keeps us grounded amidst adversity..<a>VIEW DETAIL</a></p>
  <div class="value-art" role="img" aria-label="Illustration of a presenter beside a chart board" style="background:linear-gradient(180deg,#dbe8f5 0,#f0c23c 55%,#e6edf4 100%);border-radius:8px;opacity:.8"></div>
</section>
<section class="value-card" style="top:1914px">
  <h3 class="value-title">Solution Mindset</h3>
  <p class="value-text">A solution mindset is the compass that directs our focus from problems to possibilities..<a>VIEW DETAIL</a></p>
  <div class="value-art" role="img" aria-label="Illustration of a head in profile filled with gears" style="background:radial-gradient(circle at 55% 35%,#3f5f8c 0,#bcd6ee 40%,rgba(230,237,244,0) 74%)"></div>
</section>
<section class="value-card" style="top:2157px">
  <h3 class="value-title">Generosity</h3>
  <p class="value-text">Generosity creates a virtuous cycle of goodwill, fostering a sense of unity and shared purpose among colleagues..<a>VIEW DETAIL</a></p>
  <div class="value-art" role="img" aria-label="Illustration of a person holding a heart to their chest" style="background:linear-gradient(180deg,rgba(230,237,244,0) 0,#354a77 45%,#6b2a33 100%);opacity:.8"></div>
</section>

<svg class="waves" viewBox="0 2280 1200 1071" preserveAspectRatio="none" aria-hidden="true">
  <defs>
    <linearGradient id="mist" x1="0" y1="0" x2="0" y2="1">
      <stop offset="0" stop-color="#ffffff"/>
      <stop offset="1" stop-color="#a5bdd4"/>
    </linearGradient>
    <linearGradient id="night" x1="0" y1="0" x2="0" y2="1">
      <stop offset="0" stop-color="#3e4d67"/>
      <stop offset=".55" stop-color="#4a5c78"/>
      <stop offset="1" stop-color="#60758f"/>
    </linearGradient>
  </defs>
  <rect x="0" y="2290" width="1200" height="420" fill="url(#mist)"/>
  <path d="M0 2545C120 2640 260 2680 400 2645C560 2600 650 2445 860 2442C1000 2445 1100 2495 1200 2515V2760H0Z" fill="#ffffff"/>
  <path d="M0 2725C130 2735 210 2820 310 2885C430 2960 540 2975 660 2945C800 2905 900 2860 1010 2858C1100 2856 1160 2848 1200 2840V3351H0Z" fill="#d5dbe3"/>
  <path d="M0 2725C130 2740 210 2830 310 2900C430 2985 540 3000 660 2970C800 2930 900 2880 1010 2875C1100 2870 1160 2860 1200 2852V3351H0Z" fill="url(#night)"/>
</svg>

<section class="newsletter">
  <h2>Subscribe Our Newsletter</h2>
  <p>Subscribe our newsletter to receive the latest news<br>and exclusive offers every week, No spam.</p>
  <div class="subscribe">
    <svg width="13" height="10" viewBox="0 0 13 10"><rect width="13" height="10" rx="1" fill="#8fa7bf"/><path d="M0 1l6.5 4.5L13 1" stroke="#fff" fill="none"/></svg>
    Enter email address
    <span class="subscribe-btn"><svg width="14" height="14" viewBox="0 0 14 14"><path d="M13 1 1 6l5 2 2 5z" fill="#fff"/></svg></span>
  </div>
</section>

<div class="footer-brand">Veltrion</div>
<span class="social" style="left:180px" role="img" aria-label="Social link"></span>
<span class="social" style="left:231px" role="img" aria-label="Social link"></span>
<span class="social" style="left:283px" role="img" aria-label="Social link"></span>
<span class="social" style="left:332px" role="img" aria-label="Social link"></span>
<a class="footer-contact">CONTACT US</a>

<nav class="footer-col" style="left:491px">
  <h3>Quick links</h3>
  <ul><li>Home</li><li>About Us</li><li>Services</li><li>Insights</li><li>Join Us</li><li>Contact Us</li></ul>
</nav>
<nav class="footer-col" style="left:668px">
  <h3>Our Services</h3>
  <ul><li>Business Transformation</li><li>ERP Implementations</li><li>ERP Solutions</li><li>BI and Data</li><li>Building the Right Team...</li></ul>
</nav>
<address class="footer-col" style="left:899px;font-style:normal">
  <h3>Contact info</h3>
  <div class="contact-item"><svg width="13" height="10" viewBox="0 0 13 10"><rect width="13" height="10" rx="1" fill="#f0b51a"/><path d="M0 1l6.5 4.5L13 1" stroke="#3e4d67" fill="none"/></svg><span>Email:<br>hello@veltrion-mail.com</span></div>
  <div class="contact-item"><svg width="13" height="13" viewBox="0 0 13 13"><path d="M3 0 5 3 3.5 4.5c1 2 3 4 5 5L10 8l3 2-1.5 2.5C6 12 1 7 .5 1.5z" fill="#f0b51a"/></svg><span>Phone:<br>+44 100 555 0147</span></div>
  <div class="contact-item"><svg width="11" height="14" viewBox="0 0 11 14"><path d="M5.5 0A5.5 5.5 0 0 0 0 5.5C0 9 5.5 14 5.5 14S11 9 11 5.5A5.5 5.5 0 0 0 5.5 0z" fill="#f0b51a"/><circle cx="5.5" cy="5.5" r="2" fill="#3e4d67"/></svg><span>Location:<br>Some address line goes<br>here city name</span></div>
</address>

<footer class="bottom-bar">© Veltrion Design 2023, All Rights Reserved</footer>
<div class="chat"><svg width="24" height="20" viewBox="0 0 24 20"><path d="M12 1C6 1 1 4.6 1 9c0 2.3 1.3 4.3 3.4 5.8L3 19l5-2.6c1.2.4 2.6.6 4 .6 6 0 11-3.6 11-8S18 1 12 1z" fill="#fff"/><circle cx="8" cy="9" r="1.4" fill="#f0b51a"/><circle cx="12" cy="9" r="1.4" fill="#f0b51a"/><circle cx="16" cy="9" r="1.4" fill="#f0b51a"/></svg></div>

</body>
</html>
```